Amber Ridge Photography

Internet sales of landscape photography
Some background on the name.... I'm originally from Kentucky hence the "Amber" and I now live in California wine country, hence the "Ridge." The blue coloring in the name is from the Marlow Hornets and the name "photography" is done in a bourbon lettering font. Hope this helps.
Updates
Please include email as dennis@amberridgephotography.example
Please make website www.amberridgephotography.example and ad QR code if possible.
Industry/Entity Type
Landscape
Contact Information for Business Card
Dennis Harcourt
www.amberridgephoto.example
707-555-0142
Requirements
Must have
- My design logo, all contact info :)
I like the thought of a QR Code along with the written link also.

```html
<!DOCTYPE html>
<html lang="en">
<head>
<meta charset="utf-8">
<title>Amber Ridge Photography — Business Card</title>
<link rel="stylesheet" href="https://fonts.googleapis.com/css2?family=Kalam:wght@400;700&family=Crimson+Text:wght@400&display=swap">
<style>
  :root {
    --card-blue: #0a50d8;
    --band-white: #ffffff;
    --logo-blue: #1a55e6;
    --text-white: #ffffff;
    --band-shadow: rgba(0, 12, 60, 0.75);
  }
  * { margin: 0; padding: 0; box-sizing: border-box; }
  html, body {
    width: 1200px;
    height: 702px;
    overflow: hidden;
    background: var(--card-blue);
  }
  .card {
    position: relative;
    width: 1200px;
    height: 702px;
    background: var(--card-blue);
    overflow: hidden;
  }
  .logo-band {
    position: absolute;
    left: 0;
    top: 108px;
    width: 1200px;
    height: 196px;
    background: var(--band-white);
    box-shadow: 0 -10px 22px var(--band-shadow), 0 12px 24px var(--band-shadow);
    display: flex;
    align-items: center;
    justify-content: center;
    gap: 18px;
  }
  .logo-mark {
    width: 26px;
    height: 26px;
    border-radius: 50%;
    background: var(--logo-blue);
  }
  .logo-name {
    font-family: "Kalam", cursive;
    font-weight: 700;
    font-size: 58px;
    color: var(--logo-blue);
    line-height: 1;
    padding-top: 10px;
  }
  .owner-name {
    position: absolute;
    left: 0;
    width: 1200px;
    top: 384px;
    text-align: center;
    font-family: "Kalam", cursive;
    font-weight: 400;
    font-size: 56px;
    letter-spacing: 1px;
    color: var(--text-white);
    line-height: 1;
  }
  .contact-list {
    position: absolute;
    left: 392px;
    top: 474px;
    list-style: none;
    color: var(--text-white);
  }
  .contact-item {
    display: flex;
    align-items: center;
    height: 44px;
    margin-bottom: 12px;
  }
  .contact-icon {
    width: 32px;
    height: 32px;
    margin-right: 16px;
    flex: none;
  }
  .contact-web,
  .contact-email {
    font-family: "Kalam", cursive;
    font-size: 25px;
    white-space: nowrap;
  }
  .contact-phone {
    font-family: "Crimson Text", serif;
    font-size: 28px;
  }
  .qr-code {
    position: absolute;
    left: 1000px;
    top: 478px;
    width: 150px;
    height: 150px;
    background: var(--band-white);
    border-radius: 6px;
  }
</style>
</head>
<body>
  <main class="card">
    <header class="logo-band">
      <span class="logo-mark" aria-hidden="true"></span>
      <h1 class="logo-name">Amber Ridge Photography</h1>
    </header>

    <h2 class="owner-name">DENNIS HARCOURT</h2>

    <ul class="contact-list">
      <li class="contact-item">
        <svg class="contact-icon" viewBox="0 0 34 34" aria-hidden="true" fill="none" stroke="#ffffff" stroke-width="2.2">
          <circle cx="17" cy="17" r="14"/>
          <ellipse cx="17" cy="17" rx="6" ry="14"/>
          <line x1="3" y1="17" x2="31" y2="17"/>
          <path d="M5.5 9.5 H28.5 M5.5 24.5 H28.5"/>
        </svg>
        <span class="contact-web">www.amberridgephotography.example</span>
      </li>
      <li class="contact-item">
        <svg class="contact-icon" viewBox="0 0 34 34" aria-hidden="true" fill="none" stroke="#ffffff" stroke-width="2.2">
          <rect x="3" y="7" width="28" height="20" rx="2"/>
          <path d="M3.5 8 L17 19 L30.5 8"/>
        </svg>
        <span class="contact-email">dennis@amberridgephotography.example</span>
      </li>
      <li class="contact-item">
        <svg class="contact-icon" viewBox="0 0 34 34" aria-hidden="true" fill="none" stroke="#ffffff" stroke-width="2.2">
          <rect x="9" y="1.5" width="16" height="31" rx="2.5"/>
          <line x1="9" y1="26" x2="25" y2="26"/>
          <line x1="15" y1="29.3" x2="19" y2="29.3"/>
        </svg>
        <span class="contact-phone">707 - 555 - 0142</span>
      </li>
    </ul>

    <div class="qr-code" role="img" aria-label="QR code linking to www.amberridgephotography.example"></div>
  </main>
</body>
</html>
```